Business cards and logo for kitchen and bath remodeling company

We want an elegant card but that calls attention something unique and when people see it they remember us. A log that we can use for our own. We are a kitchen and bathroom remodeling company. We are 3 partners staring the company we are located in Eastbrook Harbor District. We try to give the best experience and luxury look in our projects and we are looking to show that in our cards. I added a sample of a card I really like. I like the black and gold look but gray blue or green in a metallic look would look nice. I'm open to any color.

Target Market(s)

Home owners.

Industry/Entity Type

Construction

Contact Information for Business Card

Larchmont and Vey builders

Colors

Designer to choose colors to be used in the design.

Requirements
Must have
• Make a Logo
• Logo to be unique
• Name of company larchmont and vey builders
Nice to have
• Have a good color scheme
• Front design to connect with back of card

```html
<!DOCTYPE html>
<html lang="en">
<head>
<meta charset="utf-8">
<title>Larchmont &amp; Vey Builders — Business Cards</title>
<link href="https://fonts.googleapis.com/css2?family=Open+Sans:wght@400;600&display=swap" rel="stylesheet">
<style>
  :root {
    --stage: #3c3d3f;
    --card-dark: #2a2c30;
    --card-light: #ebebec;
    --gold: #e0a80d;
    --ink-light: #f2f2f2;
    --ink-muted: #c9cacc;
    --ink-dark: #2b2b2d;
    --ink-grey: #555658;
  }
  * { box-sizing: border-box; margin: 0; padding: 0; }
  html, body {
    width: 1200px; height: 900px; overflow: hidden;
    background: radial-gradient(ellipse at 55% 45%, #4a4b4d 0%, var(--stage) 55%, #222324 100%);
    font-family: "Open Sans", sans-serif;
  }
  .stage {
    width: 1200px; height: 900px;
    display: flex; flex-direction: column; align-items: center; justify-content: center; gap: 50px;
  }
  .card {
    width: 660px; height: 377px; border-radius: 26px; position: relative;
    box-shadow: 0 18px 40px rgba(0,0,0,0.45);
  }

  /* Back: contact side */
  .card--back { background: var(--card-dark); color: var(--ink-light); }
  .back-name {
    position: absolute; right: 56px; top: 96px;
    font-size: 38px; font-weight: 600; color: var(--ink-light); letter-spacing: -0.5px;
  }
  .back-row {
    position: absolute; left: 56px; right: 56px;
    display: flex; align-items: baseline; justify-content: space-between;
  }
  .back-row--identity { top: 190px; }
  .back-row--contact { top: 250px; font-size: 15px; color: var(--ink-muted); }
  .division-label { font-size: 16px; letter-spacing: 1px; color: var(--ink-muted); }
  .identity { font-size: 22px; color: var(--ink-light); }
  .sep { color: var(--gold); margin: 0 14px; }
  .gold-rule {
    position: absolute; left: 56px; right: 56px; top: 232px; height: 2px; background: var(--gold);
  }

  /* Front: name side */
  .card--front { background: var(--card-light); color: var(--ink-dark); }
  .front-name {
    position: absolute; left: 0; right: 0; top: 140px; text-align: center;
    font-size: 38px; font-weight: 600; color: var(--gold); letter-spacing: -0.5px;
  }
  .location {
    position: absolute; left: 0; right: 0; bottom: 70px; text-align: center;
    font-size: 14px; letter-spacing: 1px; color: var(--ink-grey);
  }
</style>
</head>
<body>
<main class="stage">
  <section class="card card--back" aria-label="Card back with contact details">
    <p class="back-name">Larchmont &amp; Vey</p>
    <div class="back-row back-row--identity">
      <span class="division-label">BUILDERS</span>
      <span class="identity"><span class="sep">|</span>Marcus Delray<span class="sep">|</span>CEO &amp; Founder</span>
    </div>
    <div class="gold-rule"></div>
    <div class="back-row back-row--contact">
      <span>206 555 0142</span>
      <span><span class="sep">|</span>info.larchmontvey.com</span>
      <span><span class="sep">|</span>www.larchmontvey.com</span>
    </div>
  </section>

  <section class="card card--front" aria-label="Card front with company name">
    <p class="front-name">Larchmont &amp; Vey Builders</p>
    <p class="location">Eastbrook Harbor District</p>
  </section>
</main>
</body>
</html>
```